Email Signature Gif Animation Design

We are looking for an interactive Email Signature to Standardize around for our growing company.

We are a commerical electrical contractor based out of North Jersey. We have a big corporate client tele and perfer a more professional fresh looking signature with titles and perhaps a suttle animation for effect.

Attached below is our company logo which is to be used prominently in the emai signature. We would consider a "refresh' of our logo design provided it does deviate too much.

We would like the tag Line "The KALV Electric Way" worked into that signature as a option.
Updates

Reviewing designs and am underwhelmed with the creativiity and designs, this is anyones prize!

Target Market(s)

Corporate / Middle Managers

Industry/Entity Type

Electrical Contracting & Engineering

Colors
FFF300
FFF600
FEFA6F
FFFEC7
FFFEE8

Requirements
Must have
• Must have, First & Last Name of Employee, Title of Employee, Office & Cell Phone Number, Email Address
Nice to have
• Gif Animation

```html
<!DOCTYPE html>
<html lang="en">
<head>
<meta charset="utf-8">
<title>Jordan Whitaker – Email Signature</title>
<link rel="stylesheet" href="https://fonts.googleapis.com/css2?family=Open+Sans:wght@400;600;800&display=swap">
<style>
  :root {
    --gold: #d4aa17;
    --gold-light: #e6c11d;
    --ink: #1c1c1c;
    --paper: #ffffff;
    --mist: #ececec;
    --photo-top: #f4f4f4;
    --photo-bottom: #2f66c8;
  }
  * { box-sizing: border-box; margin: 0; padding: 0; }
  html, body { width: 1200px; height: 402px; overflow: hidden; background: var(--paper); }
  .signature {
    position: relative; width: 1200px; height: 402px; overflow: hidden;
    font-family: "Open Sans", Arial, sans-serif; color: var(--ink);
    background: linear-gradient(115deg, var(--mist) 0%, var(--paper) 45%, var(--paper) 70%, #f3f3f3 100%);
  }
  .backdrop, .portrait-frame { position: absolute; left: 0; top: 0; }
  .employee-name {
    position: absolute; left: 61px; top: 118px;
    font-size: 38px; font-weight: 800; letter-spacing: 0.5px; line-height: 1;
  }
  .employee-title {
    position: absolute; left: 53px; top: 161px; width: 339px; height: 43px;
    background: var(--ink); padding: 3px;
  }
  .employee-title span {
    display: flex; align-items: center; justify-content: center;
    width: 100%; height: 100%; background: var(--ink);
    border: 3px solid var(--gold-light); outline: 2px solid var(--paper); outline-offset: -6px;
    color: var(--paper); font-size: 24px; font-weight: 400;
  }
  .social-links { position: absolute; left: 91px; top: 235px; display: flex; gap: 6px; }
  .social-link {
    width: 55px; height: 55px; border-radius: 50%; background: var(--ink);
    border: 5px solid var(--gold-light); box-shadow: 0 0 0 2px var(--paper), 0 0 0 4px var(--ink);
  }
  .brand {
    position: absolute; left: 419px; top: 330px; width: 371px; height: 32px;
    background: var(--paper); display: flex; align-items: center; justify-content: center; gap: 10px;
  }
  .brand-mark { width: 16px; height: 16px; background: var(--ink); }
  .brand-name { font-size: 21px; font-weight: 800; color: var(--ink); letter-spacing: 1px; text-transform: uppercase; }
  .contact-list { position: absolute; left: 819px; top: 65px; list-style: none; }
  .contact-item { display: flex; align-items: center; height: 53px; }
  .contact-icon {
    width: 48px; height: 48px; border-radius: 50%; background: var(--ink);
    border: 4px solid var(--gold-light); box-shadow: 0 0 0 2px var(--paper), 0 0 0 3px var(--ink);
    display: flex; align-items: center; justify-content: center; flex: none;
  }
  .contact-icon svg { width: 22px; height: 22px; }
  .contact-text { margin-left: 10px; font-size: 23px; font-weight: 600; }
</style>
</head>
<body>
<div class="signature">
  <svg class="backdrop" width="1200" height="402" viewBox="0 0 1200 402" aria-hidden="true">
    <polygon points="0,0 1200,0 1200,6 600,38 0,6" fill="var(--gold)"/>
    <polygon points="380,0 820,0 600,38" fill="var(--gold-light)"/>
    <polygon points="0,402 600,262 1200,402" fill="var(--gold)"/>
    <polygon points="0,402 560,285 600,268 640,285 1200,402" fill="var(--gold-light)"/>
    <polygon points="0,402 600,290 1200,402" fill="var(--ink)"/>
  </svg>

  <svg class="portrait-frame" width="1200" height="402" viewBox="0 0 1200 402">
    <polygon points="600,12 740,93 740,253 600,334 460,253 460,93" fill="var(--ink)"/>
    <polygon points="600,22 731,98 731,248 600,324 469,248 469,98" fill="var(--paper)"/>
    <polygon points="600,29 724,102 724,244 600,317 476,244 476,102" fill="var(--gold-light)"/>
    <defs>
      <linearGradient id="portrait-fill" x1="0" y1="0" x2="0" y2="1">
        <stop offset="0" stop-color="var(--photo-top)"/>
        <stop offset="0.6" stop-color="#e9dcd3"/>
        <stop offset="1" stop-color="var(--photo-bottom)"/>
      </linearGradient>
    </defs>
    <g role="img" aria-label="Portrait photo of the employee">
      <polygon points="600,38 716,106 716,240 600,308 484,240 484,106" fill="url(#portrait-fill)"/>
    </g>
  </svg>

  <h1 class="employee-name">JORDAN WHITAKER</h1>
  <p class="employee-title"><span>Support Team Leader</span></p>

  <div class="social-links" aria-label="Social profiles">
    <span class="social-link"></span>
    <span class="social-link"></span>
    <span class="social-link"></span>
    <span class="social-link"></span>
  </div>

  <div class="brand">
    <span class="brand-mark"></span>
    <span class="brand-name">KALV Electric LLC</span>
  </div>

  <ul class="contact-list">
    <li class="contact-item">
      <span class="contact-icon"><svg viewBox="0 0 24 24" fill="var(--paper)"><path d="M2 9c0-3 5-5 10-5s10 2 10 5v2h-5V9H7v2H2z"/><path d="M5 13h14v7H5z"/><circle cx="12" cy="16.5" r="2" fill="var(--ink)"/></svg></span>
      <span class="contact-text">+15550142087</span>
    </li>
    <li class="contact-item">
      <span class="contact-icon"><svg viewBox="0 0 24 24" fill="none" stroke="var(--paper)" stroke-width="2"><rect x="7" y="2" width="10" height="20" rx="2"/><circle cx="12" cy="18" r="1" fill="var(--paper)"/></svg></span>
      <span class="contact-text">+15550142088</span>
    </li>
    <li class="contact-item">
      <span class="contact-icon"><svg viewBox="0 0 24 24" fill="none" stroke="var(--paper)" stroke-width="2"><rect x="3" y="6" width="18" height="13" rx="2"/><path d="M3 7l9 7 9-7"/></svg></span>
      <span class="contact-text">jordan@kalvelectric.com</span>
    </li>
    <li class="contact-item">
      <span class="contact-icon"><svg viewBox="0 0 24 24" fill="none" stroke="var(--paper)" stroke-width="1.6"><circle cx="12" cy="12" r="9"/><ellipse cx="12" cy="12" rx="4" ry="9"/><path d="M3 12h18M5 7h14M5 17h14"/></svg></span>
      <span class="contact-text">www.kalvelectric.com</span>
    </li>
  </ul>
</div>
</body>
</html>
```